Business Card for Yachting Management Company

Need a business card design for a new yachting project management company. Attached is the logo for the company.
Our clients are large yacht owners and captains.
Design must be in the style of the logo. Modern, elegant.

Example of data to show:
Peter Hollis
Project Manager
(+34) 612 738 104
peter@quorvane.net
Quorvane Management - Meridel Tower, Office 22 - KRB - Palma de Mallorca

The data above will have to be changed (by me) for the different people in the company over the next years.

Will be printed using PrintNova (Lustre Card Series). They provide these guidelines for the size:
"the actual size of the card is 1050 x 600 pixels. However, the full bleed size is 1083 x 633 pixels, and the safe printing area is 1008 x 558 pixels."

```html
<!DOCTYPE html>
<html lang="en">
<head>
<meta charset="utf-8">
<title>Quorvane Management – Business Card</title>
<link rel="stylesheet" href="https://fonts.googleapis.com/css2?family=Montserrat:wght@400;500;700;800&display=swap">
<style>
  :root {
    --brand-blue: #0a72c2;
    --brand-grey: #8c8c8c;
    --ink: #1f1f1f;
    --paper: #ffffff;
    --backdrop: #3b3b3d;
  }
  * { margin: 0; padding: 0; box-sizing: border-box; }
  html, body { width: 1200px; height: 998px; overflow: hidden; }
  body {
    background: var(--backdrop);
    font-family: "Montserrat", sans-serif;
    position: relative;
  }
  .card {
    position: absolute;
    width: 560px;
    height: 320px;
    box-shadow: 0 10px 30px rgba(0,0,0,.45);
  }
  .card--front {
    left: 120px; top: 110px;
    background: var(--brand-blue);
    display: flex; align-items: center; justify-content: center;
  }
  .card--back {
    left: 520px; top: 560px;
    background: var(--paper);
  }
  .wordmark {
    font-weight: 800;
    line-height: 1;
    text-align: center;
  }
  .wordmark__name { display: block; font-size: 58px; letter-spacing: 1px; }
  .wordmark__sub { display: block; font-size: 20px; letter-spacing: 10px; margin-top: 10px; }
  .card--front .wordmark { color: var(--paper); }
  .card--back .wordmark {
    position: absolute; right: 36px; top: 38px;
    color: var(--brand-blue);
    text-align: right;
  }
  .card--back .wordmark__name { font-size: 38px; }
  .card--back .wordmark__sub { font-size: 14px; letter-spacing: 7px; margin-top: 6px; }
  .divider {
    position: absolute; height: 1.5px; background: var(--ink);
  }
  .divider--main { left: 230px; right: 30px; top: 138px; }
  .divider--person { left: 40px; width: 170px; top: 232px; }
  .person { position: absolute; left: 40px; top: 180px; }
  .person__name { font-size: 26px; font-weight: 800; color: var(--brand-blue); }
  .person__role { font-size: 14px; font-weight: 500; color: var(--ink); margin-top: 2px; }
  .contacts {
    position: absolute; left: 40px; top: 242px;
    list-style: none; font-size: 13px; color: var(--ink);
  }
  .contacts li { display: flex; align-items: center; gap: 8px; height: 21px; }
  .contacts svg { width: 12px; height: 12px; fill: var(--brand-blue); flex: none; }
  .address {
    position: absolute; left: 282px; top: 200px;
    font-size: 13.5px; line-height: 1.5; color: var(--ink);
  }
</style>
</head>
<body>
  <section class="card card--front">
    <div class="wordmark">
      <span class="wordmark__name">Quorvane</span>
      <span class="wordmark__sub">MANAGEMENT</span>
    </div>
  </section>

  <section class="card card--back">
    <div class="wordmark">
      <span class="wordmark__name">Quorvane</span>
      <span class="wordmark__sub">MANAGEMENT</span>
    </div>
    <div class="divider divider--main"></div>

    <div class="person">
      <p class="person__name">Peter Hollis</p>
      <p class="person__role">Project Manager</p>
    </div>
    <div class="divider divider--person"></div>

    <ul class="contacts">
      <li>
        <svg viewBox="0 0 24 24" aria-hidden="true"><path d="M6.6 10.8a15.1 15.1 0 0 0 6.6 6.6l2.2-2.2c.3-.3.7-.4 1-.2 1.1.4 2.3.6 3.6.6.6 0 1 .4 1 1V20c0 .6-.4 1-1 1A17 17 0 0 1 3 4c0-.6.4-1 1-1h3.5c.6 0 1 .4 1 1 0 1.3.2 2.5.6 3.6.1.3 0 .7-.2 1z"/></svg>
        (+34) 612 738 104
      </li>
      <li>
        <svg viewBox="0 0 24 24" aria-hidden="true"><path d="M2 5h20v14H2zm2 2v.5l8 5 8-5V7zm0 2.8V17h16V9.8l-8 5z"/></svg>
        peter@quorvane.net
      </li>
      <li>
        <svg viewBox="0 0 24 24" aria-hidden="true"><path d="M12 2a10 10 0 1 0 0 20 10 10 0 0 0 0-20zm0 2c.9 0 2.2 1.9 2.7 5H9.3C9.8 5.9 11.1 4 12 4zM4.3 10h3c-.1.7-.1 1.3-.1 2s0 1.3.1 2h-3a8 8 0 0 1 0-4zm.8 6h2.6c.3 1.3.8 2.5 1.4 3.4A8 8 0 0 1 5.1 16zm4.2 0h5.4c-.5 3.1-1.8 4-2.7 4s-2.2-.9-2.7-4zm0-6h5.4c.1.6.1 1.3.1 2s0 1.4-.1 2H9.3c-.1-.6-.1-1.3-.1-2s0-1.4.1-2zm7.4 0h3a8 8 0 0 1 0 4h-3c.1-.7.1-1.3.1-2s0-1.3-.1-2zm-.4 6h2.6a8 8 0 0 1-4 3.4c.6-.9 1.1-2.1 1.4-3.4z"/></svg>
        Your webadress here
      </li>
    </ul>

    <p class="address">
      Quorvane Management - Meridel Tower,<br>
      Office 22 - KRB - Palma de Mallorca
    </p>
  </section>
</body>
</html>
```